Halden Pelvic Care Clinics needs promo/informational brochure for marketing

Our practice has added a new practitioner and our goal is to highlight her (Nell Brisco, PA-C) in this marketing campaign while providing useful information about the practice and conditions we treat. We have also closed our Maryland Office and moved to a new NY office (7 E. 81st St. Suite 512 NY, NY 10028). I have included a copy of what our last brochure looked like as an example of what I absolutely despise:) We are removing Loretta Quince from the brochure and adding a book (also attached). We want something modern, concise, streamlined, and professional. We would love to see what you all can come up with! The sooner we get responses, the better!

Target Market(s)

physicians and patients

Industry/Entity Type

Medical

Font styles to use
Other font styles liked:
• avenir book? i'll leave it to the designer!

Colors
ffffff
cee9f5
e4daeb
000000
9d9d9d
cbcbcb

Requirements
Must have
• some sort of lotus image....or some type of background from stock images
• This is the bio of Nell Brisco to be included:
• Nell Brisco, PA
• Nell Brisco is a Nationally Certified Physician Assistant licensed in New York and Washington, DC. She graduated with honors from Wexley College of Health Sciences where she was awarded the prestigious Pemberton Award.
• Nell has been treating women with sexual dysfunction since 2010. She has extensive experience treating vaginismus, vulvodynia and other vulvovaginal disorders. She also has expertise in treating hypoactive sexual desire (low libido), arousal, and orgasmic disorders. Nell has lectured and written extensively on the topic of female sexual dysfunction and is a member of the Global Council for Research on Female Intimate Wellness.
• Nell practiced as a PA in psychiatry and orthopedic surgery before she became a female sexual medicine specialist. She is also a member of the Families of Overseas Servicemen Care Network and has volunteered in Vietnam providing medical care with Youth Hope Outreach Global (YHOG). Nell also studied at Carrow University in Australia and she spent two years living in Japan where she taught English with the Overseas Language Assistant Scheme.

```html
<!DOCTYPE html>
<html lang="en">
<head>
<meta charset="utf-8">
<title>Halden Pelvic Care Clinics – Brochure</title>
<link rel="stylesheet" href="https://fonts.googleapis.com/css2?family=Mulish:wght@300;400;600;700&display=swap">
<style>
  :root {
    --white: #ffffff;
    --lilac: #e4daeb;
    --lilac-deep: #d6c6df;
    --sky: #cee9f5;
    --ink: #000000;
    --grey: #9d9d9d;
    --grey-light: #cbcbcb;
    --stage: #ececec;
    --font: "Mulish", "Avenir", sans-serif;
  }
  * { box-sizing: border-box; margin: 0; padding: 0; }
  html, body { width: 1200px; height: 1000px; overflow: hidden; }
  body { background: var(--stage); font-family: var(--font); color: var(--ink); }

  .brochure {
    position: absolute; left: 45px; top: 70px;
    width: 1110px; height: 860px;
    display: flex;
    box-shadow: 0 6px 24px rgba(0,0,0,.15);
  }
  .panel { position: relative; width: 370px; height: 100%; overflow: hidden; background: var(--white); }
  .panel-heading { position: absolute; font-weight: 300; letter-spacing: 1px; text-transform: uppercase; }

  /* Locations panel */
  .panel-locations .panel-art { position: absolute; left: 0; top: 0; }
  .panel-locations .panel-heading { left: 40px; top: 150px; font-size: 44px; }
  .locations-list { position: absolute; right: 34px; top: 265px; width: 300px; text-align: right; }
  .practice-name { font-size: 23px; font-weight: 300; line-height: 1.2; padding-bottom: 14px; border-bottom: 1px solid var(--grey-light); margin-bottom: 26px; }
  .office { margin-bottom: 34px; }
  .office-title { font-size: 20px; font-weight: 400; }
  .office-address { font-size: 13px; line-height: 1.45; }
  .office-note { font-size: 10px; color: #444; margin-top: 8px; line-height: 1.35; }
  .locations-footer {
    position: absolute; left: 34px; right: 34px; bottom: 40px;
    border-top: 1px solid var(--grey-light); padding-top: 16px;
    font-size: 13.5px; line-height: 1.4; text-align: center;
  }

  /* Books panel */
  .panel-books { background: var(--lilac-deep); }
  .panel-books .panel-art { position: absolute; left: 0; top: 0; }
  .panel-books .panel-heading { right: 94px; top: 50px; font-size: 44px; text-align: right; line-height: 1; }
  .book-covers { position: absolute; right: 10px; top: 30px; width: 70px; display: flex; flex-direction: column; gap: 10px; }
  .book-cover { height: 112px; }
  .book-list { position: absolute; left: 26px; right: 94px; top: 190px; }
  .book { font-size: 12px; line-height: 1.5; text-align: justify; margin-bottom: 24px; }
  .book-title { font-weight: 700; }

  /* Cover panel */
  .cover-title { position: absolute; left: 30px; top: 36px; font-weight: 300; text-transform: uppercase; line-height: .95; }
  .cover-title .line-sm { display: block; font-size: 30px; }
  .cover-title .line-lg { display: block; font-size: 46px; }
  .cover-cities { position: absolute; left: 30px; top: 142px; font-size: 12px; font-weight: 600; }
  .cover-intro { position: absolute; left: 30px; right: 30px; top: 172px; font-size: 12px; line-height: 1.45; text-align: justify; }
  .bio { position: absolute; left: 30px; right: 30px; top: 272px; border-top: 1px solid var(--grey-light); padding-top: 12px; }
  .bio-name { font-size: 18px; font-weight: 400; margin-bottom: 8px; }
  .bio-photo { float: left; width: 84px; height: 104px; margin: 2px 10px 4px 0; background: linear-gradient(160deg, #d9d9d9, #8a8a8a); }
  .bio p { font-size: 10.2px; line-height: 1.42; text-align: justify; margin-bottom: 5px; }
  .lotus-art { position: absolute; left: 60px; top: 668px; width: 250px; height: 96px; border-radius: 50% 50% 10px 10px / 80% 80% 10px 10px; background: linear-gradient(180deg, var(--lilac), var(--lilac-deep)); }
  .cover-contact { position: absolute; right: 30px; bottom: 50px; font-size: 11px; text-align: right; line-height: 1.4; }
  .cover-web { position: absolute; right: 30px; bottom: 24px; font-size: 15px; font-weight: 700; }
</style>
</head>
<body>
<main class="brochure">

  <section class="panel panel-locations">
    <svg class="panel-art" width="370" height="260" viewBox="0 0 370 260" aria-hidden="true">
      <path d="M0 0 H370 V120 C300 60 200 40 110 60 C60 70 20 90 0 110 Z" fill="var(--grey-light)"/>
      <path d="M200 0 H370 V70 C320 30 260 10 200 0 Z" fill="var(--grey)"/>
      <path d="M0 140 C80 80 230 70 370 100 C330 200 200 250 40 240 C20 210 8 180 0 170 Z" fill="var(--lilac-deep)"/>
    </svg>
    <h2 class="panel-heading">Locations</h2>
    <div class="locations-list">
      <p class="practice-name">Halden Pelvic Care Clinics</p>
      <div class="office">
        <p class="office-title">Main Office</p>
        <p class="office-address">14 Larkmoor Circle NW, Suite 210<br>Washington, DC 20036<br>Phone: (202) 555-0142<br>Fax: (202) 555-0187</p>
        <p class="office-note">Across the street from<br>Larkmoor University Hospital<br>and the Larkmoor Square Metro</p>
      </div>
      <div class="office">
        <p class="office-title">New York Office:</p>
        <p class="office-address">7 E. 81st St. Suite 512<br>NY, NY 10028</p>
      </div>
    </div>
    <p class="locations-footer">Our office in Washington DC is our main office and all appointments and communications with both offices are made through this office.</p>
  </section>

  <section class="panel panel-books">
    <svg class="panel-art" width="370" height="860" viewBox="0 0 370 860" aria-hidden="true">
      <path d="M0 0 H130 C60 40 20 90 0 150 Z" fill="var(--white)"/>
      <path d="M0 860 V720 C60 780 150 830 260 860 Z" fill="var(--white)"/>
    </svg>
    <h2 class="panel-heading">Our<br>Books</h2>
    <div class="book-covers">
      <div class="book-cover" role="img" aria-label="Book cover: When Intimacy Aches" style="background:#eee4c8"></div>
      <div class="book-cover" role="img" aria-label="Book cover: Pelvic Pain in Women" style="background:linear-gradient(#1f3550,#7a93ad)"></div>
      <div class="book-cover" role="img" aria-label="Book cover: Renewing Desire" style="background:linear-gradient(#f2f2f2,#bcd9e6)"></div>
      <div class="book-cover" role="img" aria-label="Book cover: 100 Questions and Answers" style="background:linear-gradient(#f6f1f3,#e6a3c0)"></div>
    </div>
    <div class="book-list">
      <p class="book"><span class="book-title">When Intimacy Aches</span> is a guide for patients that contains up-to-date information on the diagnosis and treatment of more than 20 different causes of sexual and vulvovaginal pain. It contains an algorithm that helps a patient and her health care provider determine the specific cause and treatments of her type of vulvar pain.</p>
      <p class="book"><span class="book-title">Pelvic Pain in Women: Assessment and Care</span> is the only textbook devoted to the diagnosis and treatment of vulvar and vaginal pain disorders and disease. More than 75 world renowned scientists contributed chapters in this authoritative and comprehensive textbook.</p>
      <p class="book"><span class="book-title">Renewing Desire: 4 Paths Back to Your Libido</span> outlines a highly effective holistic approach to treating decreased sexual desire. In addition, there is essential information on the ways in which major life events such as pregnancy, menopause, and divorce can affect a woman's sexual health.</p>
      <p class="book"><span class="book-title">100 Questions &amp; Answers About Vulvar and Vaginal Cancers</span> provides practical, authoritative answers to the most common questions asked by women diagnosed with cancer of the vulva/vagina and related gynecologic diseases.</p>
    </div>
  </section>

  <section class="panel panel-cover">
    <h1 class="cover-title"><span class="line-sm">Halden Pelvic</span><span class="line-lg">Care Clinics</span></h1>
    <p class="cover-cities">Washington DC | New York City</p>
    <p class="cover-intro">For more than two decades, Halden Pelvic Care Clinics have been referral centers for the treatment of vulvodynia, sexual pain disorders, dermatologic diseases of the vulva, recurrent vulvovaginal infections, and female sexual dysfunction.</p>
    <article class="bio">
      <h2 class="bio-name">Nell Brisco, PA</h2>
      <div class="bio-photo" role="img" aria-label="Portrait of Nell Brisco, PA-C"></div>
      <p>Nell Brisco is a Nationally Certified Physician Assistant licensed in New York and Washington, DC. She graduated with honors from Wexley College of Health Sciences where she was awarded the prestigious Pemberton Award.</p>
      <p>Nell has been treating women with sexual dysfunction since 2010. She has extensive experience treating vaginismus, vulvodynia and other vulvovaginal disorders. She also has expertise in treating hypoactive sexual desire (low libido), arousal, and orgasmic disorders. Nell has lectured and written extensively on the topic of female sexual dysfunction and is a member of the Global Council for Research on Female Intimate Wellness.</p>
      <p>Nell practiced as a PA in psychiatry and orthopedic surgery before she became a female sexual medicine specialist. She is also a member of the Families of Overseas Servicemen Care Network and has volunteered in Vietnam providing medical care with Youth Hope Outreach Global (YHOG). Nell also studied at Carrow University in Australia and she spent two years living in Japan where she taught English with the Overseas Language Assistant Scheme.</p>
    </article>
    <div class="lotus-art" role="img" aria-label="Soft lilac lotus flower illustration"></div>
    <p class="cover-contact">14 Larkmoor Circle NW, Suite 210, Washington, DC 20036<br>Phone: (202) 555-0142</p>
    <p class="cover-web">www.haldenpelvic.org</p>
  </section>

</main>
</body>
</html>
```